Business Card Re-Design/Update

We'd like to update out business cards. I've included our current "Style guide" which has the colour scheme of the organisation in it. I've also included the branding files with logos etc in them.

I've also included a copy of one of our existing cards so that you can see how ugly/dated they look. I'd like a fresh modern corporate look.

Target Market(s)

These are for our clients, potential clients, industry contacts - like all business cards

Contact Information for Business Card

Name
Position
Company Address - Level 1, 52 Copperfield Road, Dunmore Qld 4071
Direct Phone
mobile
Email
Website -www.korvelit.com.au
Logo

Colors

Designer to choose colors to be used in the design.

Requirements
Must have
• Main Logo
• Cards will need to be editable to be able to personalize them for each new employee.
Nice to have
• The MapIT, HandIT, KeepIT would be okay to have if they can be sensibly and professionally added to the look without detracting from the main imagery.
• Maybe they could go on the back of the card? will leave this to your creative discretion as to whether/where they fit.
Should not have
• Should not have decorative or script fonts

```html
<!DOCTYPE html>
<html lang="en">
<head>
<meta charset="utf-8">
<title>korvelIT business card</title>
<link rel="stylesheet" href="https://fonts.googleapis.com/css2?family=Carlito:wght@400;700&family=Roboto:wght@400;500;700&display=swap">
<style>
  :root {
    --brand-red: #d81f26;
    --tab-red: #c8202a;
    --ink: #3a3a3c;
    --text: #333333;
    --paper: #ffffff;
    --page: #ffffff;
  }
  html, body {
    margin: 0;
    padding: 0;
    width: 1200px;
    height: 1200px;
    overflow: hidden;
    background: var(--page);
  }
  .canvas {
    position: relative;
    width: 1200px;
    height: 1200px;
  }
  .card {
    position: absolute;
    left: 209px;
    width: 781px;
    height: 447px;
    box-shadow: 0 2px 6px rgba(0,0,0,0.35);
  }
  .card--front {
    top: 103px;
    background: radial-gradient(ellipse at 50% 40%, #e21e27 0%, var(--brand-red) 60%, #d31e25 100%);
  }
  .card--back {
    top: 606px;
    background: var(--paper);
  }

  /* Front */
  .front-brand {
    position: absolute;
    left: 0;
    right: 0;
    top: 272px;
    transform: translateY(-50%);
    display: flex;
    align-items: center;
    justify-content: center;
    gap: 22px;
    margin-top: -0px;
  }
  .front-brand__mark {
    width: 62px;
    height: 62px;
    background: var(--paper);
  }
  .front-brand__name {
    font-family: "Roboto", sans-serif;
    font-weight: 500;
    font-size: 86px;
    letter-spacing: -1px;
    color: var(--paper);
    line-height: 1;
  }
  .front-web {
    position: absolute;
    left: 0;
    right: 0;
    top: 378px;
    text-align: center;
    font-family: "Roboto", sans-serif;
    font-size: 23px;
    color: var(--ink);
  }
  .front-web__domain { color: var(--paper); }

  /* Back */
  .tab {
    position: absolute;
    left: 0;
    top: 90px;
    width: 45px;
    height: 58px;
    background: var(--tab-red);
    border-radius: 0 8px 8px 0;
  }
  .person {
    position: absolute;
    left: 63px;
    top: 82px;
    font-family: "Carlito", sans-serif;
  }
  .person__name {
    margin: 0;
    font-size: 40px;
    font-weight: 700;
    color: var(--brand-red);
    line-height: 1;
  }
  .person__role {
    margin: 4px 0 0;
    font-size: 19.5px;
    color: var(--text);
  }
  .address {
    position: absolute;
    left: 63px;
    top: 191px;
    margin: 0;
    font-family: "Carlito", sans-serif;
    font-style: normal;
    font-size: 22px;
    line-height: 30px;
    color: var(--brand-red);
  }
  .contact-group {
    position: absolute;
    font-family: "Carlito", sans-serif;
    font-size: 20px;
    line-height: 26px;
    color: var(--text);
  }
  .contact-group--mobile { left: 63px; top: 293px; }
  .contact-group--phone { left: 63px; top: 357px; }
  .contact-group--web { left: 479px; top: 362px; }
  .contact-group p { margin: 0; }
  .icon {
    position: absolute;
    fill: none;
    stroke: var(--brand-red);
  }
  .icon--mobile { left: 33px; top: 304px; }
  .icon--phone { left: 33px; top: 370px; }
  .icon--globe { left: 439px; top: 374px; }

  .back-brand {
    position: absolute;
    left: 560px;
    top: 118px;
    width: 190px;
    display: flex;
    flex-direction: column;
    align-items: center;
    gap: 18px;
  }
  .back-brand__mark {
    width: 150px;
    height: 150px;
    background: var(--brand-red);
  }
  .back-brand__name {
    font-family: "Carlito", sans-serif;
    font-weight: 700;
    font-size: 36px;
    color: var(--brand-red);
    line-height: 1;
  }
</style>
</head>
<body>
<div class="canvas">

  <section class="card card--front" aria-label="Card front">
    <div class="front-brand">
      <div class="front-brand__mark"></div>
      <span class="front-brand__name">korvelIT</span>
    </div>
    <p class="front-web" style="margin:0">www.<span class="front-web__domain">korvelit</span>.com.au</p>
  </section>

  <section class="card card--back" aria-label="Card back">
    <div class="tab"></div>
    <div class="person">
      <h1 class="person__name">Dana Whitfield</h1>
      <p class="person__role">Business Development Manager</p>
    </div>

    <address class="address">18/9 Larkspur Avenue,<br>Fernvale QLD 4306</address>

    <svg class="icon icon--mobile" width="24" height="28" viewBox="0 0 24 28" aria-hidden="true">
      <rect x="7" y="4" width="10" height="20" rx="1.5" stroke-width="2"/>
      <line x1="10" y1="21" x2="14" y2="21" stroke-width="1.5"/>
      <path d="M4 5 q-2 3 0 6 M20 5 q2 3 0 6" stroke-width="1"/>
    </svg>
    <div class="contact-group contact-group--mobile">
      <p>+61 (0)412 555 018</p>
      <p>+61 (0)7 3555 0142</p>
    </div>

    <svg class="icon icon--phone" width="24" height="26" viewBox="0 0 24 26" aria-hidden="true">
      <path d="M5 4 l4 -1 l2 5 l-3 2 q2 5 6 8 l2 -3 l5 2 l-1 4 q-4 2 -10 -4 q-6 -6 -5 -13 z" fill="var(--brand-red)" stroke="none"/>
      <path d="M14 4 q5 1 6 6 M14 8 q2 0.5 2.5 2.5" stroke-width="1.5"/>
    </svg>
    <div class="contact-group contact-group--phone">
      <p>+61 (0)7 3555 0100</p>
      <p>+61 (0)7 3555 0199</p>
    </div>

    <div class="back-brand">
      <div class="back-brand__mark"></div>
      <span class="back-brand__name">korvelIT</span>
    </div>

    <svg class="icon icon--globe" width="28" height="28" viewBox="0 0 28 28" aria-hidden="true">
      <circle cx="14" cy="14" r="11.5" stroke-width="1.6"/>
      <ellipse cx="14" cy="14" rx="5" ry="11.5" stroke-width="1.4"/>
      <line x1="2.5" y1="14" x2="25.5" y2="14" stroke-width="1.4"/>
      <path d="M4.5 8 h19 M4.5 20 h19" stroke-width="1.4"/>
    </svg>
    <div class="contact-group contact-group--web">
      <p>dwhitfield@korvelit.com.au</p>
      <p>www.korvelit.com.au</p>
    </div>
  </section>

</div>
</body>
</html>
```